Meridian Sound Wellness LLC Card Design

Need business card with a logo for a hearing aid sales and audiology business. We have two Hearing Instrument Specialists and one Audiologist on staff. Over 25 years in business. Locally owned and operated. Financing available. Most insurances accepted.

Meridian Sound Wellness LLC
48730 W Linden Row, Suite 9
Spokane, WA 99481
509-617-2085
www.meridiansoundnorth.example

Manager
Tobias Wrenfield HIS COHC
License #81729046

Target Market(s)

50yr old + people with a hearing loss.

Industry/Entity Type

Business

Contact Information for Business Card

48730 W Linden Row, Suite 9
Spokane, WA 99481
509-617-2085
www.meridiansoundnorth.example

Manager
Tobias Wrenfield HIS COHC
NRPL #81729046

Font styles to use
Serif
Sans Serif

Requirements
Must have
• Business name, Tobias's name and title(s) and contact information, License #, web address
Nice to have
Should not have

```html
<!DOCTYPE html>
<html lang="en">
<head>
<meta charset="UTF-8">
<title>Meridian Sound Wellness LLC – Business Card</title>
<link rel="stylesheet" href="https://fonts.googleapis.com/css2?family=Lato:wght@400;700;900&family=Roboto:wght@400;500;700&family=Caveat:wght@400&display=swap">
<style>
  :root {
    --navy: #2b2a78;
    --orange: #f07a1a;
    --ink-soft: #4a4f8f;
    --card: #ffffff;
    --stage: #1d1d1d;
    --rule: #9a9ab8;
  }
  * { margin: 0; padding: 0; box-sizing: border-box; }
  html, body {
    width: 1200px;
    height: 800px;
    overflow: hidden;
  }
  body {
    background: var(--stage);
    position: relative;
    font-family: "Lato", Arial, sans-serif;
    color: var(--navy);
  }
  .card {
    position: absolute;
    top: 283px;
    width: 429px;
    height: 238px;
    background: var(--card);
    overflow: hidden;
  }
  .card--front { left: 110px; }
  .card--back { left: 638px; }

  .brand {
    position: absolute;
    display: flex;
    align-items: center;
    gap: 12px;
  }
  .brand__mark {
    width: 56px;
    height: 56px;
    flex: none;
  }
  .brand__name {
    font-family: "Roboto", Arial, sans-serif;
    font-weight: 700;
    font-size: 16.5px;
    letter-spacing: 0.2px;
    color: var(--navy);
    white-space: nowrap;
  }
  .card--front .brand { left: 46px; top: 89px; }
  .card--back .brand { left: 46px; top: 41px; }

  .tagline {
    position: absolute;
    right: 48px;
    top: 134px;
    font-family: "Caveat", cursive;
    font-size: 15px;
    color: var(--navy);
  }
  .services {
    position: absolute;
    left: 0;
    right: 0;
    top: 200px;
    text-align: center;
    font-size: 9.6px;
    line-height: 13px;
    color: var(--navy);
  }

  .contact {
    position: absolute;
    top: 140px;
    left: 0;
    right: 0;
    font-family: "Roboto", Arial, sans-serif;
    font-size: 11px;
    line-height: 13px;
  }
  .contact__person {
    position: absolute;
    right: 225px;
    top: 0;
    text-align: right;
    white-space: nowrap;
  }
  .contact__name { font-weight: 700; font-size: 11.5px; color: var(--navy); }
  .contact__title { color: var(--orange); }
  .contact__license { color: var(--ink-soft); font-size: 10.5px; }
  .contact__divider {
    position: absolute;
    left: 213px;
    top: -3px;
    width: 1px;
    height: 49px;
    background: var(--rule);
  }
  .contact__address {
    position: absolute;
    left: 223px;
    top: 0;
    color: var(--navy);
    white-space: nowrap;
  }
  .contact__label { color: var(--orange); }

  .web-band {
    position: absolute;
    left: 0;
    right: 0;
    bottom: 0;
    height: 18px;
    background: var(--navy);
    color: #ffffff;
    font-weight: 700;
    font-size: 10px;
    line-height: 18px;
    text-align: center;
    letter-spacing: 0.2px;
  }
</style>
</head>
<body>

  <section class="card card--front" aria-label="Business card front">
    <div class="brand">
      <svg class="brand__mark" viewBox="0 0 56 56" aria-hidden="true">
        <circle cx="28" cy="28" r="26" fill="var(--navy)"/>
      </svg>
      <span class="brand__name">MERIDIAN SOUND WELLNESS LLC</span>
    </div>
    <p class="tagline">Over 25 years in business</p>
    <p class="services">
      Two Hearing Instrument Specialists and one Audiologist on staff.<br>
      Locally owned and operated | Financing available | Most insurances accepted.
    </p>
  </section>

  <section class="card card--back" aria-label="Business card back">
    <div class="brand">
      <svg class="brand__mark" viewBox="0 0 56 56" aria-hidden="true">
        <circle cx="28" cy="28" r="26" fill="var(--navy)"/>
      </svg>
      <span class="brand__name">MERIDIAN SOUND WELLNESS LLC</span>
    </div>

    <div class="contact">
      <div class="contact__person">
        <div class="contact__name">Tobias Wrenfield HIS COHC</div>
        <div class="contact__title">Manager</div>
        <div class="contact__license">License #81729046</div>
      </div>
      <span class="contact__divider"></span>
      <div class="contact__address">
        <div>48730 W Linden Row, Suite 9</div>
        <div>Spokane, WA 99481</div>
        <div><span class="contact__label">P:</span> 509-617-2085</div>
      </div>
    </div>

    <div class="web-band">www.meridiansoundnorth.example</div>
  </section>

</body>
</html>
```